A start-up named "Corvath Therapeutics" - needs a new PowerPoint design

We need a new PowerPoint Design for an early-stage start-up named "Corvath Therapeutics" seeking to disrupt the current approach towards drug discovery within aging disorders.

We would like to build on Corvath's legacy, the founder of the modern science of genetics, by employing a multidisciplinary approach, experimenting, and providing elderly patients the attention they deserve.

We have selected the suffix "therapeutics" intentionally as it stands for (a medicine) the treatment of disease; the science of healing. Alzheimer’s treatment is a huge, urgent, unmet need:
- Shift from a disease-management system to a preventive medicine system
- Focus on increasing the health span, not only the life span

Target Market(s)

Pharma/ Biotech Executives Medical Institutions Healthcare professionals (MDs, nurses, payors, pharmacists, etc.) Patients

Industry/Entity Type

Healthcare

Other font styles liked:
• Celias

Colors
0054AA
0677BA
7BADD7
CADEEF
E8F1F8
E54698
E96AAD
F1A4CE
F9D9EA
FCEFF6
A7469A
B969AE
D3A5CF
EDDBEB
F8F0F9
6B429C
8869AF
B7A5CE
E3DAEB
F3F0F8

Requirements
Must have
• - differentiate from other companies named after Corvath - differentiate from other Pharma/ Biotech companies
Nice to have
• simplicity/ minimalist logo vivid colors gradient 3D Life-Sciences inspired Simple geometry Balance
Should not have
• mascot/ emblem watermark logo animated ink style nature-inspired inventive typography artistic chaos

```html
<!DOCTYPE html>
<html lang="en">
<head>
<meta charset="utf-8">
<title>Corvath Therapeutics – Presentation Template</title>
<link href="https://fonts.googleapis.com/css2?family=Montserrat:wght@500;600;700&family=Roboto:wght@400;500;700&display=swap" rel="stylesheet">
<style>
:root{
  --page-bg:#e9eaed;
  --white:#ffffff;
  --magenta:#e54698;
  --magenta-deep:#b53a86;
  --plum:#a7469a;
  --violet:#6b429c;
  --violet-deep:#4c2a7e;
  --ink:#1d1b22;
  --text:#55525c;
  --muted:#8d8a93;
  --row-grey:#f0f0f2;
  --band-grey:#efeff1;
}
*{box-sizing:border-box;margin:0;padding:0}
html,body{width:1200px;height:3639px;overflow:hidden}
body{background:var(--page-bg);font-family:"Roboto",sans-serif;color:var(--text);position:relative}
.slide{position:absolute;left:45px;width:1110px;height:624px;background:var(--white);overflow:hidden}
.slide--cover{top:76px;background:linear-gradient(120deg,#b8337f 0%,#9a3590 45%,#6e2f9a 100%)}
.slide--about{top:792px}
.slide--process{top:1506px;background:linear-gradient(135deg,#f4f4f6,#e6e7ea 60%,#f1f1f3)}
.slide--faq{top:2221px}
.slide--table{top:2936px;background:linear-gradient(160deg,#fafafb,#eeeff1)}

/* cover */
.cover-photo{position:absolute;inset:0;background:radial-gradient(circle at 25% 40%,rgba(255,120,190,.25),transparent 45%),radial-gradient(circle at 80% 20%,rgba(120,90,220,.25),transparent 40%)}
.cover-brand{position:absolute;top:118px;left:0;width:100%;text-align:center;font-family:"Montserrat",sans-serif;font-weight:600;font-size:52px;color:var(--white);letter-spacing:1px}
.cover-brand .mark{display:inline-block;width:44px;height:44px;border:3px solid var(--white);margin-right:18px;vertical-align:-4px}
.cover-title{position:absolute;top:288px;width:100%;text-align:center;font-family:"Montserrat",sans-serif;font-weight:700;font-size:55px;color:var(--white);letter-spacing:1.5px}
.cover-sub{position:absolute;top:392px;width:100%;text-align:center;font-family:"Montserrat",sans-serif;font-weight:600;font-size:30px;color:var(--white);letter-spacing:19px;padding-left:19px}
.cover-social{position:absolute;top:467px;left:0;width:100%;display:flex;justify-content:center;gap:14px}
.cover-social span{width:38px;height:38px;border:1.5px solid rgba(255,255,255,.85);border-radius:50%}

/* shared header / footer */
.slide-header{position:absolute;top:0;left:0;width:1110px;height:57px}
.slide-header svg{position:absolute;inset:0}
.header-brand{position:absolute;left:88px;top:13px;font-family:"Montserrat",sans-serif;font-weight:600;font-size:22px;color:var(--white)}
.header-brand .mark{display:inline-block;width:22px;height:22px;border:2px solid var(--white);margin-right:9px;vertical-align:-3px}
.header-title{position:absolute;right:87px;top:14px;font-family:"Montserrat",sans-serif;font-weight:600;font-size:26px;color:var(--white);letter-spacing:.5px}
.slide-footer{position:absolute;left:88px;right:87px;top:573px;display:flex;justify-content:space-between;font-size:11px;color:#3a3840}
.slide-footer .page{font-weight:700;font-size:10px;padding-top:5px}
.slide-rule{position:absolute;left:0;bottom:0;width:100%;height:4px;background:linear-gradient(90deg,var(--magenta) 0%,#8b3d9c 20%,var(--violet-deep) 40%,#8e4aa8 60%,var(--violet) 80%,var(--magenta) 100%)}

/* about */
.content-band{position:absolute;left:3px;top:151px;width:565px;height:48px;background:var(--band-grey);text-align:right;padding:15px 48px 0 0;font-family:"Montserrat",sans-serif;font-weight:600;font-size:17px;color:var(--ink)}
.content-text{position:absolute;left:88px;top:216px;width:432px;font-size:11px;line-height:21.5px;text-align:justify;text-align-last:right;color:#4a4750}
.content-photo{position:absolute;left:574px;top:138px;width:449px;height:363px;border-radius:10px;overflow:hidden;background:linear-gradient(160deg,#3a2ab8 0%,#b04ac0 45%,#e2609c 60%,#3d1d72 100%)}
.content-photo .caption{position:absolute;left:0;bottom:0;width:100%;height:54px;background:rgba(20,12,50,.55);color:var(--white);font-weight:700;font-size:13px;text-align:center;line-height:54px}

/* process */
.process-title{position:absolute;top:117px;width:100%;text-align:center;font-family:"Montserrat",sans-serif;font-weight:600;font-size:25px;color:var(--ink)}
.process-hub{position:absolute;left:423px;top:219px;width:264px;height:264px;border-radius:50%;background:var(--violet-deep);padding:14px}
.process-hub div{width:100%;height:100%;border-radius:50%;background:radial-gradient(circle at 45% 45%,#a33da8,#3b1d56 70%,#140b20)}
.step{position:absolute;width:68px;height:68px;border-radius:50%;background:var(--white);box-shadow:0 2px 6px rgba(0,0,0,.18);padding:5px}
.step b{display:block;width:58px;height:58px;border-radius:50%;background:var(--violet-deep);color:var(--white);font-family:"Montserrat",sans-serif;font-weight:600;font-size:25px;text-align:center;line-height:58px}
.step-text{position:absolute;width:270px;font-size:11px;font-weight:500;line-height:17px;color:#3d3a44}
.step-text--left{text-align:right}

/* faq */
.qa{position:absolute;width:470px}
.qa-row{position:relative;height:42px;margin-bottom:10px;padding-left:72px}
.qa-key{position:absolute;left:0;top:0;width:49px;height:42px;color:var(--white);font-family:"Montserrat",sans-serif;font-weight:600;font-size:24px;text-align:center;line-height:42px}
.qa-key--q{background:var(--violet)}
.qa-key--a{background:var(--magenta)}
.qa-q{font-size:11px;font-weight:700;line-height:17px;color:var(--ink);padding-top:4px}
.qa-a{font-size:11px;line-height:17px;color:var(--muted);padding-top:4px}

/* table */
.table-rail{position:absolute;left:140px;top:180px;width:65px;height:310px}
.table-grid{position:absolute;left:120px;top:151px;width:895px}
.table-head{display:flex;margin-left:102px;gap:4px;height:37px}
.table-head div{flex:1;color:var(--white);font-weight:700;font-size:12px;text-align:center;line-height:37px}
.table-head .c1{background:var(--magenta)}
.table-head .c2{background:var(--violet)}
.table-head .c3{background:#913c96}
.table-row{display:flex;height:39.5px;margin-top:0;font-size:12px;color:#4d4a52;padding-left:102px}
.table-row:nth-child(odd){background:var(--row-grey)}
.table-row div{flex:1;text-align:center;line-height:39.5px}
.table-body{margin-top:10px}
</style>
</head>
<body>

<!-- Cover -->
<section class="slide slide--cover">
  <div class="cover-photo" role="img" aria-label="Soft-focus DNA helix backdrop in magenta and violet"></div>
  <div class="cover-brand"><span class="mark"></span>Corvath Therapeutics</div>
  <h1 class="cover-title">CORVATH THERAPEUTICS</h1>
  <p class="cover-sub">SUB TITLE GOES HERE</p>
  <div class="cover-social" aria-label="Social links"><span></span><span></span><span></span><span></span></div>
</section>

<!-- Content slide -->
<section class="slide slide--about">
  <header class="slide-header">
    <svg width="1110" height="57" viewBox="0 0 1110 57"><defs><linearGradient id="hg1" x1="0" x2="1"><stop offset="0" stop-color="#b23a83"/><stop offset=".55" stop-color="#8a3590"/><stop offset="1" stop-color="#55287f"/></linearGradient></defs><polygon points="0,57 60,0 1055,0 1110,57" fill="url(#hg1)"/><polygon points="1040,0 1060,0 1110,50 1110,57" fill="#3e1f66"/></svg>
    <div class="header-brand"><span class="mark"></span>Corvath Therapeutics</div>
    <div class="header-title">YOUR TITLE GOES HERE</div>
  </header>
  <div class="content-band">CONTENT HERE</div>
  <p class="content-text">Sed ut perspiciatis unde omnis iste natus error sit voluptatem accusantium doloremque laudantium, totam rem aperiam, eaque ipsa quae ab illo inventore veritatis et quasi architecto beatae vitae dicta sunt explicabo. Nemo enim ipsam voluptatem quia voluptas sit aspernatur aut odit aut fugit, sed quia consequuntur magni dolores eos qui ratione voluptatem sequi nesciunt. Neque porro quisquam est, qui dolorem ipsum quia dolor sit amet, consectetur, adipisci velit, sed quia non numquam eius modi tempora incidunt ut labore et dolore magnam aliquam quaerat voluptatem. Ut enim ad minima veniam, quis nostrum exercitationem ullam corporis suscipit laboriosam, nisi ut aliquid ex ea commodi consequatur? Quis autem vel eum iure reprehenderit qui in ea voluptate velit esse quam nihil molestiae consequatur, vel illum qui dolorem eum Sed ut perspiciatis unde omnis iste natus error sit voluptatem accusantium doloremque laudantium, totam rem aperiam, eaque ipsa quae ab illo inventore veritatis et quasi architecto beatae vitae dicta sunt explicabo.</p>
  <div class="content-photo" role="img" aria-label="Glowing DNA double helix over a field of coloured light particles">
    <div class="caption">ADD YOUR CONTENT HERE</div>
  </div>
  <footer class="slide-footer"><span>© 2022 Corvath Therapeutics. All Rights Reserved</span><span class="page">Page No | 02</span></footer>
  <div class="slide-rule"></div>
</section>

<!-- Process slide -->
<section class="slide slide--process">
  <header class="slide-header">
    <svg width="1110" height="57" viewBox="0 0 1110 57"><defs><linearGradient id="hg2" x1="0" x2="1"><stop offset="0" stop-color="#b23a83"/><stop offset=".55" stop-color="#8a3590"/><stop offset="1" stop-color="#55287f"/></linearGradient></defs><polygon points="0,57 60,0 1055,0 1110,57" fill="url(#hg2)"/><polygon points="1040,0 1060,0 1110,50 1110,57" fill="#3e1f66"/></svg>
    <div class="header-brand"><span class="mark"></span>Corvath Therapeutics</div>
    <div class="header-title">YOUR TITLE GOES HERE</div>
  </header>
  <h2 class="process-title">YOUR TITLE GOES HERE</h2>
  <svg width="1110" height="624" viewBox="0 0 1110 624" style="position:absolute;inset:0">
    <path d="M422 212 A200 200 0 0 0 376 480 L452 498" fill="none" stroke="#e54698" stroke-width="1.5" stroke-dasharray="3 4"/>
    <path d="M688 212 A200 200 0 0 1 734 480 L680 488" fill="none" stroke="#6b429c" stroke-width="1.5" stroke-dasharray="3 4"/>
    <circle cx="422" cy="212" r="3.5" fill="#e54698"/><circle cx="452" cy="498" r="3.5" fill="#e54698"/>
    <circle cx="688" cy="212" r="3.5" fill="#6b429c"/><circle cx="680" cy="488" r="3.5" fill="#6b429c"/>
  </svg>
  <div class="process-hub" role="img" aria-label="Purple network illustration of a DNA strand"><div></div></div>
  <div class="step" style="left:342px;top:223px"><b>04</b></div>
  <div class="step" style="left:312px;top:315px"><b>05</b></div>
  <div class="step" style="left:342px;top:411px"><b>06</b></div>
  <div class="step" style="left:695px;top:223px"><b>01</b></div>
  <div class="step" style="left:724px;top:315px"><b>02</b></div>
  <div class="step" style="left:695px;top:411px"><b>03</b></div>
  <p class="step-text step-text--left" style="left:60px;top:241px">Sed ut perspiciatis unde omnis iste natus error sit laudantium, totam rem aperiam</p>
  <p class="step-text step-text--left" style="left:30px;top:333px">Sed ut perspiciatis unde omnis iste natus error sit laudantium, totam rem aperiam</p>
  <p class="step-text step-text--left" style="left:60px;top:429px">Sed ut perspiciatis unde omnis iste natus error sit laudantium, totam rem aperiam</p>
  <p class="step-text" style="left:776px;top:241px">Sed ut perspiciatis unde omnis iste natus err sit voluptatem accusantium doloremque</p>
  <p class="step-text" style="left:805px;top:333px">Sed ut perspiciatis unde omnis iste natus err sit voluptatem accusantium doloremque</p>
  <p class="step-text" style="left:776px;top:429px">Sed ut perspiciatis unde omnis iste natus err sit voluptatem accusantium doloremque</p>
  <footer class="slide-footer"><span>© 2022 Corvath Therapeutics. All Rights Reserved</span><span class="page">Page No | 03</span></footer>
  <div class="slide-rule"></div>
</section>

<!-- FAQ slide -->
<section class="slide slide--faq">
  <header class="slide-header">
    <svg width="1110" height="57" viewBox="0 0 1110 57"><defs><linearGradient id="hg3" x1="0" x2="1"><stop offset="0" stop-color="#b23a83"/><stop offset=".55" stop-color="#8a3590"/><stop offset="1" stop-color="#55287f"/></linearGradient></defs><polygon points="0,57 60,0 1055,0 1110,57" fill="url(#hg3)"/><polygon points="1040,0 1060,0 1110,50 1110,57" fill="#3e1f66"/></svg>
    <div class="header-brand"><span class="mark"></span>Corvath Therapeutics</div>
    <div class="header-title">YOUR TITLE GOES HERE</div>
  </header>
  <div class="qa" style="left:86px;top:127px">
    <div class="qa-row"><span class="qa-key qa-key--q">Q</span><p class="qa-q">Lorem ipsum dolor sit amet, consectetur adipiscing elit, sed do eiusmod tempor incididunt ut labore ?</p></div>
    <div class="qa-row"><span class="qa-key qa-key--a">A</span><p class="qa-a">Sed ut perspiciatis unde omnis iste natus error sit voluptatem accusan tium doloremque laudantium, totam rem aperiam</p></div>
  </div>
  <div class="qa" style="left:86px;top:266px">
    <div class="qa-row"><span class="qa-key qa-key--q">Q</span><p class="qa-q">Lorem ipsum dolor sit amet, consectetur adipiscing elit, sed do eiusmod tempor incididunt ut labore ?</p></div>
    <div class="qa-row"><span class="qa-key qa-key--a">A</span><p class="qa-a">Sed ut perspiciatis unde omnis iste natus error sit voluptatem accusan tium doloremque laudantium, totam rem aperiam</p></div>
  </div>
  <div class="qa" style="left:86px;top:405px">
    <div class="qa-row"><span class="qa-key qa-key--q">Q</span><p class="qa-q">Lorem ipsum dolor sit amet, consectetur adipiscing elit, sed do eiusmod tempor incididunt ut labore ?</p></div>
    <div class="qa-row"><span class="qa-key qa-key--a">A</span><p class="qa-a">Sed ut perspiciatis unde omnis iste natus error sit voluptatem accusan tium doloremque laudantium, totam rem aperiam</p></div>
  </div>
  <div class="qa" style="left:576px;top:127px">
    <div class="qa-row"><span class="qa-key qa-key--q">Q</span><p class="qa-q">Lorem ipsum dolor sit amet, consectetur adipiscing elit, sed do eiusmod tempor incididunt ut labore ?</p></div>
    <div class="qa-row"><span class="qa-key qa-key--a">A</span><p class="qa-a">Sed ut perspiciatis unde omnis iste natus error sit voluptatem accusan tium doloremque laudantium, totam rem aperiam</p></div>
  </div>
  <div class="qa" style="left:576px;top:266px">
    <div class="qa-row"><span class="qa-key qa-key--q">Q</span><p class="qa-q">Lorem ipsum dolor sit amet, consectetur adipiscing elit, sed do eiusmod tempor incididunt ut labore ?</p></div>
    <div class="qa-row"><span class="qa-key qa-key--a">A</span><p class="qa-a">Sed ut perspiciatis unde omnis iste natus error sit voluptatem accusan tium doloremque laudantium, totam rem aperiam</p></div>
  </div>
  <div class="qa" style="left:576px;top:405px">
    <div class="qa-row"><span class="qa-key qa-key--q">Q</span><p class="qa-q">Lorem ipsum dolor sit amet, consectetur adipiscing elit, sed do eiusmod tempor incididunt ut labore ?</p></div>
    <div class="qa-row"><span class="qa-key qa-key--a">A</span><p class="qa-a">Sed ut perspiciatis unde omnis iste natus error sit voluptatem accusan tium doloremque laudantium, totam rem aperiam</p></div>
  </div>
  <footer class="slide-footer"><span>© 2022 Corvath Therapeutics. All Rights Reserved</span><span class="page">Page No | 04</span></footer>
  <div class="slide-rule"></div>
</section>

<!-- Table slide -->
<section class="slide slide--table">
  <header class="slide-header">
    <svg width="1110" height="57" viewBox="0 0 1110 57"><defs><linearGradient id="hg4" x1="0" x2="1"><stop offset="0" stop-color="#b23a83"/><stop offset=".55" stop-color="#8a3590"/><stop offset="1" stop-color="#55287f"/></linearGradient></defs><polygon points="0,57 60,0 1055,0 1110,57" fill="url(#hg4)"/><polygon points="1040,0 1060,0 1110,50 1110,57" fill="#3e1f66"/></svg>
    <div class="header-brand"><span class="mark"></span>Corvath Therapeutics</div>
    <div class="header-title">YOUR TITLE GOES HERE</div>
  </header>
  <div class="table-grid">
    <div class="table-head"><div class="c1">TEXT HERE</div><div class="c2">TEXT HERE</div><div class="c3">TEXT HERE</div></div>
    <div class="table-body">
      <div class="table-row"><div>Add Contents Title Here</div><div>Add Contents Title Here</div><div>Add Contents Title Here</div></div>
      <div class="table-row"><div>Add Contents Title Here</div><div>Add Contents Title Here</div><div>Add Contents Title Here</div></div>
      <div class="table-row"><div>Add Contents Title Here</div><div>Add Contents Title Here</div><div>Add Contents Title Here</div></div>
      <div class="table-row"><div>Add Contents Title Here</div><div>Add Contents Title Here</div><div>Add Contents Title Here</div></div>
      <div class="table-row"><div>Add Contents Title Here</div><div>Add Contents Title Here</div><div>Add Contents Title Here</div></div>
      <div class="table-row"><div>Add Contents Title Here</div><div>Add Contents Title Here</div><div>Add Contents Title Here</div></div>
      <div class="table-row"><div>Add Contents Title Here</div><div>Add Contents Title Here</div><div>Add Contents Title Here</div></div>
    </div>
  </div>
  <svg class="table-rail" viewBox="0 0 65 310" aria-hidden="true">
    <polygon points="12,0 65,0 65,310 12,310 12,292 0,282 12,282" fill="#6b2f7f"/>
    <polygon points="0,282 12,282 12,292" fill="#3e1d4f"/>
    <g fill="#ffffff" stroke="#ffffff">
      <circle cx="38" cy="31" r="5" fill="none" stroke-width="2"/><path d="M38 20v3M38 39v3M27 31h3M46 31h3" stroke-width="2"/>
      <path d="M32 65h12l-3 10h-6z" stroke="none"/><circle cx="38" cy="60" r="4" stroke="none"/>
      <path d="M38 118l-9-9a5 5 0 0 1 9-6a5 5 0 0 1 9 6z" stroke="none"/>
      <rect x="29" y="144" width="18" height="10" rx="2" stroke="none"/><circle cx="38" cy="140" r="3" stroke="none"/>
      <circle cx="38" cy="189" r="5" stroke="none"/><path d="M30 181l16 16M46 181l-16 16" stroke-width="2"/>
      <path d="M38 219v18M29 228h18M32 222l12 12M44 222l-12 12" stroke-width="1.8"/>
      <circle cx="38" cy="267" r="4" stroke="none"/><path d="M38 256v4M38 274v4M28 267h4M44 267h4" stroke-width="2"/>
    </g>
  </svg>
  <footer class="slide-footer"><span>© 2022 Corvath Therapeutics. All Rights Reserved</span><span class="page">Page No | 05</span></footer>
  <div class="slide-rule"></div>
</section>

</body>
</html>
```